women's junior contemporary apparel company.
We are looking for a business card that represents our urban design aesthetic. We would like to keep it simple and modern/contemporary.
the name of the company is 'v-lumen'.

we've attached a font style but you are not limited solely to use this font. All suggestions are welcomed.

Industry/Entity Type

Business

```html
<!DOCTYPE html>
<html lang="en">
<head>
<meta charset="utf-8">
<title>v-lumen business card</title>
<link href="https://fonts.googleapis.com/css2?family=Comic+Neue:wght@400;700&display=swap" rel="stylesheet">
<style>
  :root {
    --backdrop: #2b2b2b;
    --card-dark: #151515;
    --card-light: #f4f4f4;
    --accent: #f1c40f;
    --accent-soft: #d9b21a;
    --ink: #3c3c3c;
    --ink-muted: #555555;
  }
  * { box-sizing: border-box; margin: 0; padding: 0; }
  html, body { width: 1200px; height: 1000px; overflow: hidden; }
  body {
    background: var(--backdrop);
    font-family: "Comic Neue", "Comic Sans MS", cursive;
    position: relative;
  }
  .card {
    position: absolute;
    left: 250px;
    width: 700px;
    height: 400px;
    border-radius: 4px;
    box-shadow: 0 10px 30px rgba(0,0,0,0.45);
    overflow: hidden;
  }
  .card--front { top: 60px; background: var(--card-dark); }
  .card--back { top: 540px; background: var(--card-light); }

  .front-wordmark {
    position: absolute;
    left: 0; right: 0; top: 0; bottom: 0;
    display: flex;
    align-items: center;
    justify-content: center;
    font-weight: 700;
    font-size: 138px;
    color: var(--accent-soft);
    letter-spacing: 2px;
  }

  .back-wordmark {
    position: absolute;
    left: 215px;
    top: 30px;
    font-weight: 700;
    font-size: 82px;
    color: var(--ink);
    letter-spacing: 1px;
  }
  .holder {
    position: absolute;
    left: 52px;
    top: 150px;
  }
  .holder-name {
    font-weight: 700;
    font-size: 30px;
    color: var(--accent);
    line-height: 1;
  }
  .holder-role {
    margin-top: 4px;
    font-size: 17px;
    color: var(--ink-muted);
    letter-spacing: 6px;
  }
  .rule {
    position: absolute;
    height: 1px;
    background: var(--accent);
  }
  .rule--top { left: 40px; right: 40px; top: 222px; }
  .rule--bottom { left: 400px; right: 40px; top: 362px; }
  .contact {
    position: absolute;
    left: 52px;
    top: 234px;
    font-size: 19px;
    color: var(--ink);
    line-height: 1.45;
  }
  .label { font-weight: 700; color: var(--accent); margin-right: 6px; }
  .location {
    position: absolute;
    left: 420px;
    top: 300px;
    font-size: 19px;
    color: var(--ink);
    line-height: 1.3;
  }
</style>
</head>
<body>
  <section class="card card--front" aria-label="Card front">
    <div class="front-wordmark">v-lumen</div>
  </section>

  <section class="card card--back" aria-label="Card back">
    <div class="back-wordmark">v-lumen</div>
    <div class="holder">
      <p class="holder-name">Lina Farouk</p>
      <p class="holder-role">Designer</p>
    </div>
    <div class="rule rule--top"></div>
    <div class="contact">
      <p><span class="label">Mob.</span>014-258-369</p>
      <p><span class="label">Email.</span>hello@vlumen.co</p>
    </div>
    <div class="location">
      <p><span class="label">Loc.</span>48 Kora St.,</p>
      <p>cairo</p>
    </div>
    <div class="rule rule--bottom"></div>
  </section>
</body>
</html>
```